Business card design for a debt inventory management software company

We need a business card design to help us move into the next phase of our business. We developed an innovative solution to help companies collect their bad debts. We are moving into a new era and branching out into new industries. We are open to design ideas but would like that they have a similar feel/look to our website and include our logo. https://www.lumoryx.com

Target Market(s)

Finance Industry, Telecom Industry, Utility Industry, Healthcare Industry, Insurance Industry

Industry/Entity Type

Software

Contact Information for Business Card

Include Name, Title, Phone, Email, website, address, and logo

Font styles to use
Sans Serif

Colors

Designer to choose colors to be used in the design.

Requirements
Must have
• A similar look and feel to our website. https://www.lumoryx.com

```html
<!DOCTYPE html>
<html lang="en">
<head>
<meta charset="UTF-8">
<title>Lumoryx Software – Business Card</title>
<link href="https://fonts.googleapis.com/css2?family=Raleway:wght@400;500;700&display=swap" rel="stylesheet">
<style>
  :root {
    --stage: #232323;
    --card: #3b4468;
    --card-light: #46507a;
    --white: #ffffff;
    --text-soft: #e9ebf3;
    --accent: #f4c21f;
  }
  * { margin: 0; padding: 0; box-sizing: border-box; }
  html, body { width: 1200px; height: 900px; overflow: hidden; }
  body {
    background: var(--stage);
    font-family: "Raleway", sans-serif;
    position: relative;
  }
  .card {
    position: absolute;
    left: 250px;
    width: 700px;
    height: 400px;
    background: var(--card);
    overflow: hidden;
  }
  .card--front { top: 36px; }
  .card--back { top: 464px; }
  .card__texture {
    position: absolute; inset: 0;
    background: radial-gradient(ellipse at 70% 20%, var(--card-light), var(--card) 70%);
  }
  .brand {
    position: absolute;
    display: flex;
    align-items: center;
    gap: 14px;
    color: var(--white);
    font-weight: 400;
    letter-spacing: 1px;
  }
  .brand__dot {
    width: 22px; height: 22px;
    border-radius: 50%;
    background: var(--accent);
  }
  .card--front .brand { left: 50%; top: 50%; transform: translate(-50%, -50%); font-size: 40px; }
  .card--back .brand { left: 40px; top: 168px; font-size: 30px; }
  .card--back .brand__dot { width: 18px; height: 18px; }
  .divider {
    position: absolute;
    left: 368px; top: 56px;
    width: 2px; height: 270px;
    background: var(--white);
  }
  .contact {
    position: absolute;
    left: 396px; top: 58px;
    color: var(--text-soft);
  }
  .contact__name {
    color: var(--accent);
    font-weight: 700;
    font-size: 28px;
    letter-spacing: 2px;
    text-transform: uppercase;
  }
  .contact__title { font-size: 17px; font-weight: 500; margin-bottom: 14px; letter-spacing: 1px; }
  .contact__list { list-style: none; font-size: 17px; letter-spacing: 1px; line-height: 28px; }
  .contact__list li { display: flex; align-items: center; gap: 10px; }
  .contact__list svg { width: 13px; height: 13px; fill: none; stroke: var(--accent); stroke-width: 2; }
  .contact__address { margin-top: 10px; font-size: 17px; line-height: 26px; letter-spacing: 0.5px; color: var(--white); }
</style>
</head>
<body>
  <section class="card card--front">
    <div class="card__texture" role="img" aria-label="Faint geometric pattern on navy card background"></div>
    <div class="brand"><span class="brand__dot"></span><span class="brand__name">Lumoryx Software</span></div>
  </section>

  <section class="card card--back">
    <div class="card__texture" role="img" aria-label="Faint geometric pattern on navy card background"></div>
    <div class="brand"><span class="brand__dot"></span><span class="brand__name">Lumoryx Software</span></div>
    <div class="divider"></div>
    <div class="contact">
      <h1 class="contact__name">Daniel Harrow</h1>
      <p class="contact__title">Director</p>
      <ul class="contact__list">
        <li><svg viewBox="0 0 16 16"><path d="M4 2l3 3-2 2c1 2 2 3 4 4l2-2 3 3-2 2C7 14 2 9 2 4z"/></svg>330.555.0142</li>
        <li><svg viewBox="0 0 16 16"><rect x="3" y="6" width="10" height="8"/><rect x="5" y="2" width="6" height="4"/></svg>330.555.0187</li>
        <li><svg viewBox="0 0 16 16"><rect x="2" y="4" width="12" height="9"/><path d="M2 4l6 5 6-5"/></svg>info@lumoryx.com</li>
        <li><svg viewBox="0 0 16 16"><circle cx="8" cy="8" r="6"/><path d="M2 8h12M8 2c-3 3-3 9 0 12M8 2c3 3 3 9 0 12"/></svg>www.lumoryx.com</li>
      </ul>
      <p class="contact__address">48 Linden Park Road,<br>Suite 210, Hudson, Ohio 44236</p>
    </div>
  </section>
</body>
</html>
```